EASY AND SIMPLE MONEY: Make an A6 flyer for Wendelpunkt

For the design use the logo of our company [login to view URL]
and use the two pictures Merk and Merk 2 as background.
Do as you want, you can use other pictures, other designs etc
BONUS: if you use a red lion as mascot!

We need the following written on our flyer (CHECK SPELLING):
- Mir flécken Ären Computer
- Mir flécken Ären Handy
- Mir hëllefen Iech mam Computer
- Mir maachen Är Internetsäit
- Mir erstellen Apps fir Iech

And down I need to have this written:
Internet: [login to view URL] Tel.: +352698305214 E-mail: wendelpunktluxembourg@[login to view URL]

```html
<!DOCTYPE html>
<html lang="lb">
<head>
<meta charset="utf-8">
<title>Wendelpunkt Flyer</title>
<link href="https://fonts.googleapis.com/css2?family=Lato:wght@300;400&display=swap" rel="stylesheet">
<style>
  :root {
    --white: #ffffff;
    --lavender: #8a8af7;
    --navy: #262a78;
    --footer-navy: #25285f;
    --ink: #141414;
    --brand-blue: #3ea7ec;
    --sky-top: #b9bcc0;
    --sky-low: #d9dadc;
    --steel: #5b5550;
    --mascot-ring: #2a2d5c;
  }
  * { margin: 0; padding: 0; box-sizing: border-box; }
  html, body { width: 933px; height: 1200px; overflow: hidden; background: var(--white); }
  .flyer {
    position: relative;
    width: 933px;
    height: 1200px;
    overflow: hidden;
    font-family: 'Lato', sans-serif;
    background: var(--white);
  }
  .flyer__shapes { position: absolute; inset: 0; width: 933px; height: 1200px; }
  .brand-mark {
    position: absolute;
    left: 88px;
    top: 456px;
    width: 100px;
    height: 100px;
    background: var(--brand-blue);
  }
  .brand {
    position: absolute;
    left: 55px;
    top: 570px;
    font-family: 'Lato', sans-serif;
    font-weight: 400;
    font-size: 28px;
    letter-spacing: 0.5px;
    color: var(--ink);
  }
  .services {
    position: absolute;
    left: 53px;
    top: 858px;
    list-style: none;
  }
  .services__item {
    display: flex;
    align-items: center;
    height: 27px;
    margin-bottom: 16.5px;
    color: var(--white);
    font-weight: 300;
    font-size: 16px;
  }
  .services__tick { width: 27px; height: 27px; margin-right: 10px; flex: none; }
  .mascot {
    position: absolute;
    left: 641px;
    top: 923px;
    width: 156px;
    height: 156px;
    border-radius: 50%;
    border: 4px solid var(--mascot-ring);
    background: radial-gradient(circle at 50% 55%, #b9d9b0 0%, #e8efe6 45%, var(--white) 75%);
  }
  .footer {
    position: absolute;
    left: 0;
    top: 1146px;
    width: 933px;
    height: 54px;
    background: var(--footer-navy);
    display: flex;
    align-items: center;
    color: var(--white);
    font-size: 13px;
    font-weight: 400;
  }
  .footer__item { position: absolute; display: flex; align-items: center; gap: 10px; }
  .footer__item--phone { left: 52px; }
  .footer__item--mail { left: 330px; }
  .footer__item--web { left: 673px; }
  .footer__icon { width: 22px; height: 22px; flex: none; }
</style>
</head>
<body>
<div class="flyer">
  <svg class="flyer__shapes" viewBox="0 0 900 1157" preserveAspectRatio="none">
    <defs>
      <linearGradient id="industryTones" x1="0" y1="0" x2="0" y2="1">
        <stop offset="0" stop-color="var(--sky-top)"/>
        <stop offset="0.3" stop-color="var(--sky-low)"/>
        <stop offset="0.45" stop-color="#8d8680"/>
        <stop offset="0.7" stop-color="var(--steel)"/>
        <stop offset="1" stop-color="#7f8a6a"/>
      </linearGradient>
    </defs>
    <path class="photo-area" role="img" aria-label="Photo of the former blast furnaces and new buildings of an industrial site under a cloudy sky"
          d="M0,60 C170,330 470,530 900,568 L900,0 L0,0 Z" fill="url(#industryTones)"/>
    <path d="M0,60 C170,330 470,530 900,568" fill="none" stroke="var(--lavender)" stroke-width="9"/>
    <path class="body-fill" d="M0,655 C300,640 600,610 900,565 L900,1105 L0,1105 Z" fill="var(--lavender)"/>
    <path class="white-swoosh" d="M0,60 C170,330 470,530 900,572 C600,610 300,640 0,650 Z" fill="var(--white)"/>
    <path class="navy-band" d="M0,645 C300,640 600,610 900,572 L900,582 C620,650 320,705 0,706 Z" fill="var(--navy)"/>
  </svg>

  <div class="brand-mark" aria-hidden="true"></div>
  <div class="brand">WENDELPUNKT</div>

  <ul class="services">
    <li class="services__item"><svg class="services__tick" viewBox="0 0 27 27"><circle cx="13.5" cy="13.5" r="13.5" fill="#2a2d6a"/><path d="M8 14 L12 18 L19.5 9.5" fill="none" stroke="#fff" stroke-width="3" stroke-linecap="round" stroke-linejoin="round"/></svg>Mir flécken Ären Computer</li>
    <li class="services__item"><svg class="services__tick" viewBox="0 0 27 27"><circle cx="13.5" cy="13.5" r="13.5" fill="#2a2d6a"/><path d="M8 14 L12 18 L19.5 9.5" fill="none" stroke="#fff" stroke-width="3" stroke-linecap="round" stroke-linejoin="round"/></svg>Mir flécken Ären Handy</li>
    <li class="services__item"><svg class="services__tick" viewBox="0 0 27 27"><circle cx="13.5" cy="13.5" r="13.5" fill="#2a2d6a"/><path d="M8 14 L12 18 L19.5 9.5" fill="none" stroke="#fff" stroke-width="3" stroke-linecap="round" stroke-linejoin="round"/></svg>Mir hëllefen Iech mam Computer</li>
    <li class="services__item"><svg class="services__tick" viewBox="0 0 27 27"><circle cx="13.5" cy="13.5" r="13.5" fill="#2a2d6a"/><path d="M8 14 L12 18 L19.5 9.5" fill="none" stroke="#fff" stroke-width="3" stroke-linecap="round" stroke-linejoin="round"/></svg>Mir maachen Är Internetsäit</li>
    <li class="services__item"><svg class="services__tick" viewBox="0 0 27 27"><circle cx="13.5" cy="13.5" r="13.5" fill="#2a2d6a"/><path d="M8 14 L12 18 L19.5 9.5" fill="none" stroke="#fff" stroke-width="3" stroke-linecap="round" stroke-linejoin="round"/></svg>Mir erstellen Apps fir Iech</li>
  </ul>

  <div class="mascot" role="img" aria-label="Cartoon illustration of a tired desktop computer mascot"></div>

  <footer class="footer">
    <div class="footer__item footer__item--phone">+352698305214
      <svg class="footer__icon" viewBox="0 0 22 22"><circle cx="11" cy="11" r="10" fill="none" stroke="#fff" stroke-width="1.5"/><path d="M7.5 6.5 L9.3 6.3 L10.2 8.8 L9 9.8 C9.7 11.3 10.7 12.3 12.2 13 L13.2 11.8 L15.7 12.7 L15.5 14.5 C11 15 7 11 7.5 6.5 Z" fill="#fff"/></svg>
    </div>
    <div class="footer__item footer__item--mail">wendelpunktluxembourg@postfach.lu
      <svg class="footer__icon" viewBox="0 0 22 22"><circle cx="11" cy="11" r="10" fill="none" stroke="#fff" stroke-width="1.5"/><rect x="6" y="7.5" width="10" height="7" fill="#fff"/><path d="M6 7.5 L11 11.5 L16 7.5" fill="none" stroke="#25285f" stroke-width="1"/></svg>
    </div>
    <div class="footer__item footer__item--web">www.wendelpunkt.siteblog.lu
      <svg class="footer__icon" viewBox="0 0 22 22"><circle cx="11" cy="11" r="10" fill="none" stroke="#fff" stroke-width="1.5"/><circle cx="11" cy="11" r="5.5" fill="none" stroke="#fff" stroke-width="1.2"/><ellipse cx="11" cy="11" rx="2.3" ry="5.5" fill="none" stroke="#fff" stroke-width="1"/><line x1="5.5" y1="11" x2="16.5" y2="11" stroke="#fff" stroke-width="1"/></svg>
    </div>
  </footer>
</div>
</body>
</html>
```